FUN, COLORFUL, AND FAMILY CONCERT THAT CALLED BELLOMARA

A fun, colorful and modern poster. The theme this year is green and yellow, but please use other colors such as Neon or new combinations, patterns, cool design pattern or even splashes background. The name of the event is BELLOMARA. I want the Bellomara name to stand out and the date as well. Make the website name highlighted so other will go to the website and buy tickets to the concert. The date will be July, 11th, 2015. start time will be 4pm. Location at The Harlow Center @ Kessington University. Tickets will be $15 Adults $12 kids under 12 $5 under 5. I will send the old poster to give you a idea, but I want this year poster to be more of an eye catcher. I am still on the hiring process for the 4 bands will have so leave space for that as well. You can use circle or square or patterns for the photos. I like clear colors as well on the background or patterns. BE YOURSELF & CREATE THIS POSTER FROM YOUR HEART <3

Target Market(s)

everyone.

Industry/Entity Type

University

Font styles to use
Serif

Requirements
Must have
• the small bellomara logo on the bottom corner. Real people having fun in a concert ..please clear picture nothing blurry!
Nice to have
• brighter and white on the letters for Belomara. highlight Bellomara name, date, and the website (make those bigger). You can use circle, splashes, cool patterns for the date.
Should not have
• be boring ... it needs to be fun and an eye catcher

```html
<!DOCTYPE html>
<html lang="en">
<head>
<meta charset="utf-8">
<title>Bellomara Family Concert</title>
<link href="https://fonts.googleapis.com/css2?family=Anton&display=swap" rel="stylesheet">
<style>
  :root {
    --ink: #0b0b0b;
    --logo-green: #1f3d1c;
    --sun-yellow: #f6f02a;
    --sun-pale: #fffbb0;
    --leaf-green: #2fb24a;
    --lime: #b8e02c;
    --deep-green: #1e9a3c;
    --paper: #ffffff;
    --lavender: #e6c9ee;
    --lilac: #c9a6dc;
    --violet: #7b4fb0;
    --plum: #5a3296;
  }
  * { margin: 0; padding: 0; box-sizing: border-box; }
  html, body { width: 848px; height: 1200px; overflow: hidden; background: var(--paper); }
  .poster {
    position: relative;
    width: 848px;
    height: 1200px;
    overflow: hidden;
    font-family: "Anton", "Impact", sans-serif;
    color: var(--ink);
    text-transform: uppercase;
  }

  /* green top field */
  .green-field {
    position: absolute; left: 0; top: 0; width: 848px; height: 470px;
    background: linear-gradient(180deg, var(--leaf-green) 0%, #52c43b 45%, var(--lime) 75%, #c6e86a 100%);
  }
  .green-texture {
    position: absolute; left: 0; top: 190px; width: 848px; height: 280px;
    background:
      radial-gradient(ellipse at 30% 40%, rgba(240,250,120,0.55), transparent 60%),
      radial-gradient(ellipse at 75% 60%, rgba(255,255,200,0.35), transparent 55%),
      linear-gradient(180deg, rgba(170,220,40,0.6), rgba(200,235,80,0.4));
  }
  .side-strip {
    position: absolute; right: 0; top: 0; width: 128px; height: 230px;
    background: var(--deep-green);
  }

  /* sunburst header */
  .sun-panel {
    position: absolute; left: 112px; top: 0; width: 608px; height: 192px;
    background: radial-gradient(ellipse at 55% 20%, var(--sun-pale) 0%, #fff66a 35%, var(--sun-yellow) 75%);
  }
  .brand-name {
    position: absolute; left: 112px; top: 68px; width: 608px;
    text-align: center;
    font-size: 96px; line-height: 1; font-weight: 400;
    color: var(--logo-green);
    letter-spacing: 1px;
  }

  /* large title */
  .headline-echo {
    position: absolute; left: 0; top: 238px; width: 848px;
    text-align: center;
    font-size: 168px; line-height: 1;
    color: var(--deep-green);
    opacity: 0.85;
    letter-spacing: 2px;
  }

  /* white info band */
  .info-band {
    position: absolute; left: 0; top: 462px; width: 848px; height: 258px;
    background: linear-gradient(180deg, #fdeae6 0%, var(--paper) 18%, var(--paper) 100%);
  }
  .rule { position: absolute; left: 45px; width: 760px; height: 7px; background: var(--ink); }
  .rule--top { top: 474px; }
  .rule--bottom { top: 630px; }
  .event-date {
    position: absolute; left: 0; top: 484px; width: 848px;
    text-align: center;
    font-size: 128px; line-height: 1.08;
    letter-spacing: 3px;
  }
  .event-date sup { font-size: 46px; vertical-align: 62px; line-height: 0; }
  .event-venue {
    position: absolute; left: 0; top: 645px; width: 848px;
    text-align: center;
    font-size: 34px; line-height: 1.2;
    letter-spacing: 1.6px;
  }

  /* purple lower field */
  .purple-field {
    position: absolute; left: 0; top: 712px; width: 848px; height: 488px;
    background: linear-gradient(180deg, var(--lavender) 0%, var(--lilac) 20%, var(--violet) 50%, var(--plum) 100%);
  }
  .crowd {
    position: absolute; left: 0; top: 712px; width: 848px; height: 240px;
    background: linear-gradient(180deg, rgba(123,79,176,0) 0%, rgba(110,70,170,0.45) 60%, rgba(110,70,170,0) 100%);
  }

  /* band photo spaces */
  .band-row {
    position: absolute; left: 0; top: 735px; width: 848px;
    display: flex; justify-content: space-evenly;
  }
  .band-slot {
    width: 150px; height: 150px; border-radius: 50%;
    background: radial-gradient(circle at 40% 35%, #efd9f5 0%, #b58fd6 100%);
    border: 5px solid var(--paper);
  }

  /* website highlight */
  .website {
    position: absolute; left: 154px; top: 900px; width: 540px; height: 52px;
    background: var(--sun-yellow);
    text-align: center;
    font-size: 32px; line-height: 52px;
    letter-spacing: 1.5px;
    text-transform: lowercase;
  }

  .price { position: absolute; left: 0; width: 848px; text-align: center; line-height: 1; }
  .price--adult { top: 968px; font-size: 80px; letter-spacing: 3px; }
  .price--kids  { top: 1058px; font-size: 56px; letter-spacing: 2px; }
  .price--small { top: 1128px; font-size: 40px; letter-spacing: 1.5px; }

  /* corner mark */
  .corner-mark {
    position: absolute; right: 24px; bottom: 22px;
    display: flex; align-items: center; gap: 8px;
    font-size: 22px; line-height: 1;
    color: var(--paper);
    letter-spacing: 1px;
  }
  .corner-mark__dot { width: 16px; height: 16px; border-radius: 50%; background: var(--sun-yellow); }
</style>
</head>
<body>
  <main class="poster">
    <div class="green-field"></div>
    <div class="green-texture" role="img" aria-label="Soft yellow and green smoky light texture"></div>
    <div class="side-strip"></div>

    <div class="sun-panel" role="img" aria-label="Yellow sunburst rays behind the event name"></div>
    <h1 class="brand-name">BELLOMARA</h1>

    <div class="headline-echo" aria-hidden="true">BELLOMARA</div>

    <section class="info-band"></section>
    <div class="rule rule--top"></div>
    <p class="event-date">JULY/11<sup>TH</sup>/2015</p>
    <div class="rule rule--bottom"></div>
    <p class="event-venue">4PM/THE HARLOW CENTER @ KESSINGTON UNIVERSITY</p>

    <div class="purple-field"></div>
    <div class="crowd" role="img" aria-label="Silhouettes of a concert crowd with raised hands"></div>

    <div class="band-row">
      <div class="band-slot" role="img" aria-label="Photo of band one"></div>
      <div class="band-slot" role="img" aria-label="Photo of band two"></div>
      <div class="band-slot" role="img" aria-label="Photo of band three"></div>
      <div class="band-slot" role="img" aria-label="Photo of band four"></div>
    </div>

    <p class="website">tickets at www.bellomara.com</p>

    <p class="price price--adult">$15 ADULTS</p>
    <p class="price price--kids">$12 KIDS UNDER 12</p>
    <p class="price price--small">$5 UNDER 5</p>

    <div class="corner-mark">
      <span class="corner-mark__dot"></span>
      <span>BELLOMARA</span>
    </div>
  </main>
</body>
</html>
```